Seniors Massage Care Business Needs a New Website

Hello,
We require a website to be designed and coded. The design and coding must be high quality. Our website host has requested files be in static HTML format if possible.

The business is a mobile massage service for seniors (elderly people). The designer should emphasise that the business is a mobile service

The website will only have 4 pages.

1. Home- very simple layout and minimal information
2. Massage Services- this houses all of the information about the different services etc.
3. Contact Us-
4. ホーム (this is the Japanese symbol for 'home')- All of the information on the home page (section 1) will be translated into Japanese and uploaded to the brief for the designers to insert.

There is no requirement for an online booking, just contact information. The words 'Make a Booking' can be used and should lead customers to the 'Contact Us' page.

I have attached the business logo in multiple formats for designers to use.

I will upload more content and images to use for the website by the end of this week.

Thank you. I look forward to working with the successful candidate.

Target Market(s)

People aged 50+ years

Industry/Entity Type

Massage Therapy

Coding

Coded - Design and coding required

Number of Pages Required

4 page

Font styles to use
Sans Serif

Colors
74cabd
abd036
9ccb3b
f6faec
ffffff

Requirements
Must have
• Copyright free images and photos that we have taken. Both are important.
• Simple and inviting design.
Nice to have
• Colours of the logo incorporated.
Should not have
• This business is not a massage shop, so no images of massage shops or day salons required.
• Not too much imagery as the design needs to be simple.

```html
<!DOCTYPE html>
<html lang="en">
<head>
<meta charset="utf-8">
<title>Golden Years Massage – Mobile Massage for Seniors</title>
<link rel="stylesheet" href="https://fonts.googleapis.com/css2?family=Marcellus&family=Montserrat:wght@400;600&family=Lato:wght@400&family=Noto+Sans+JP:wght@500&display=swap">
<style>
  :root {
    --green: #9ccb3b;
    --green-light: #abd036;
    --teal: #74cabd;
    --cream: #f6faec;
    --band: #eff6e1;
    --page: #f9fbf3;
    --ink: #232323;
    --ink-soft: #3a3a3a;
    --white: #ffffff;
    --rule: #b9b9b9;
    --link-dark: #3a9a1a;
  }
  * { box-sizing: border-box; margin: 0; padding: 0; }
  html, body { width: 730px; height: 1200px; overflow: hidden; }
  body {
    position: relative;
    background: var(--page);
    color: var(--ink);
    font-family: "Lato", sans-serif;
  }
  a { color: inherit; text-decoration: none; }

  /* Header */
  .brand {
    position: absolute; display: flex; flex-direction: column; align-items: center;
    font-family: "Marcellus", sans-serif; color: var(--green);
  }
  .brand-mark { width: 34px; height: 34px; border-radius: 50%; border: 2px solid var(--green); }
  .brand-name { font-size: 15px; letter-spacing: .3px; margin-top: 8px; white-space: nowrap; }
  .header-brand { left: 41px; top: 8px; width: 170px; }

  .contact-item { position: absolute; top: 13px; display: flex; gap: 8px; align-items: center; font-size: 8px; line-height: 11px; color: var(--ink); white-space: nowrap; }
  .contact-item svg { width: 22px; height: 22px; flex: none; }
  .lang {
    position: absolute; left: 643px; top: 22px; width: 55px; height: 15px;
    border: 1px solid #cfcfcf; font-size: 9px; color: #888; display: flex; align-items: center;
  }
  .lang span { padding: 0 6px; border-right: 1px solid #cfcfcf; line-height: 13px; }
  .lang svg { margin-left: 6px; }

  .main-nav { position: absolute; top: 55px; left: 356px; font-family: "Marcellus", sans-serif; font-size: 10.5px; letter-spacing: 1px; }
  .main-nav a { position: absolute; white-space: nowrap; }
  .main-nav .current { color: var(--green); border-bottom: 1px solid var(--green); padding-bottom: 3px; }
  .jp { font-family: "Noto Sans JP", sans-serif; letter-spacing: 0; }

  /* Slider */
  .slider { position: absolute; left: 41px; top: 82px; width: 657px; height: 276px; }
  .slide-visual {
    width: 100%; height: 100%;
    background: linear-gradient(100deg, #e9e3d6 0%, #f1ede4 40%, #e4ddd0 62%, #5f6b62 80%, #46524a 100%);
  }
  .slide-caption { position: absolute; left: 24px; top: 168px; font-family: "Marcellus", sans-serif; font-weight: 400; font-size: 13.5px; line-height: 18px; color: var(--ink); }
  .slide-arrow { position: absolute; top: 124px; width: 22px; height: 28px; display: flex; align-items: center; justify-content: center; }
  .slide-arrow.prev { left: 1px; background: rgba(255,255,255,.55); }
  .slide-arrow.next { right: 1px; background: rgba(90,90,90,.7); }
  .slider-shadow { position: absolute; left: 60px; top: 358px; width: 620px; height: 18px; border-radius: 50%; background: radial-gradient(ellipse at top, rgba(0,0,0,.35), rgba(0,0,0,0) 70%); }
  .dots { position: absolute; top: 380px; left: 339px; display: flex; gap: 5px; }
  .dots i { width: 9px; height: 9px; border-radius: 50%; border: 1.5px solid var(--teal); }
  .dots i.on { background: var(--green); border-color: var(--green); }

  /* Sections */
  .section-title { position: absolute; left: 0; width: 730px; text-align: center; font-family: "Marcellus", sans-serif; font-weight: 400; font-size: 24px; letter-spacing: 2px; color: var(--ink); }
  .section-title em { font-style: normal; color: var(--green); }
  .title-rule { position: absolute; height: 5px; }
  .title-rule::before { content: ""; position: absolute; left: 0; right: 0; top: 2px; border-top: 1px dotted var(--rule); }
  .title-rule::after { content: ""; position: absolute; left: 50%; width: 153px; margin-left: -76px; top: 0; height: 4px; background: var(--green); }

  .lead { position: absolute; left: 36px; width: 658px; top: 474px; text-align: center; font-family: "Montserrat", sans-serif; font-weight: 600; font-size: 11.8px; line-height: 22px; }
  .body-copy { position: absolute; left: 40px; width: 660px; top: 534px; text-align: center; font-family: "Montserrat", sans-serif; font-size: 8.6px; line-height: 16px; color: var(--ink-soft); }
  .read-more-main { position: absolute; top: 593px; left: 0; width: 730px; text-align: center; font-family: "Marcellus", sans-serif; font-size: 11px; color: var(--link-dark); }

  .services-band { position: absolute; left: 0; top: 639px; width: 730px; height: 338px; background: var(--band); }
  .service { position: absolute; top: 729px; width: 160px; text-align: center; }
  .service-photo { width: 130px; height: 130px; border-radius: 50%; margin: 0 auto; }
  .service h3 { font-family: "Marcellus", sans-serif; font-weight: 400; font-size: 15px; letter-spacing: 1px; margin-top: 11px; }
  .service p { font-family: "Lato", sans-serif; font-size: 8px; line-height: 12px; margin-top: 4px; color: var(--ink); }
  .service a { display: block; margin-top: 7px; font-family: "Marcellus", sans-serif; font-size: 10px; color: var(--green); letter-spacing: .5px; }

  /* Footer */
  .footer-brand { left: 265px; top: 1012px; width: 200px; }
  .footer-brand .brand-mark { width: 42px; height: 42px; }
  .footer-brand .brand-name { font-size: 17px; margin-top: 10px; }
  .footer-nav { position: absolute; top: 1112px; left: 0; width: 730px; display: flex; justify-content: center; gap: 34px; font-family: "Marcellus", sans-serif; font-size: 10.5px; letter-spacing: 1px; }
  .social { position: absolute; top: 1148px; left: 341px; display: flex; gap: 5px; }
  .social i { width: 13px; height: 13px; border-radius: 50%; background: var(--teal); }
  .copyright { position: absolute; left: 0; top: 1172px; width: 730px; height: 28px; background: var(--green); color: var(--white); font-size: 8px; display: flex; align-items: center; justify-content: center; }
</style>
</head>
<body>

<header>
  <a class="brand header-brand" href="#">
    <span class="brand-mark"></span>
    <span class="brand-name">GOLDEN YEARS MASSAGE</span>
  </a>

  <div class="contact-item" style="left:392px">
    <svg viewBox="0 0 24 24" fill="none" stroke="#9ccb3b" stroke-width="2" stroke-linecap="round" stroke-linejoin="round"><path d="M22 16.9v3a2 2 0 0 1-2.2 2 19.8 19.8 0 0 1-8.6-3.1 19.5 19.5 0 0 1-6-6A19.8 19.8 0 0 1 2.1 4.2 2 2 0 0 1 4.1 2h3a2 2 0 0 1 2 1.7c.1.9.4 1.8.7 2.7a2 2 0 0 1-.5 2.1L8 9.8a16 16 0 0 0 6 6l1.3-1.3a2 2 0 0 1 2.1-.4c.9.3 1.8.6 2.7.7a2 2 0 0 1 1.7 2z"/></svg>
    <div>Call Us:<br>555-010-2468</div>
  </div>
  <div class="contact-item" style="left:493px">
    <svg viewBox="0 0 24 24" fill="none" stroke="#9ccb3b" stroke-width="2" stroke-linejoin="round"><rect x="2" y="5" width="20" height="14"/><path d="M2 5l10 8 10-8"/></svg>
    <div>Mail Us:<br>info@goldenyears.example</div>
  </div>
  <div class="lang"><span>ENG</span><svg width="8" height="5" viewBox="0 0 8 5"><path d="M0 0l4 4 4-4" fill="none" stroke="#888"/></svg></div>

  <nav class="main-nav">
    <a class="current" href="#" style="left:0">HOME</a>
    <a href="#" style="left:67px">MASSAGE SERVICES</a>
    <a class="jp" href="#" style="left:201px">ホーム</a>
    <a href="#" style="left:273px">CONTACT US</a>
  </nav>
</header>

<section class="slider">
  <div class="slide-visual" role="img" aria-label="Therapist giving a back massage to a client lying on a white towel"></div>
  <h2 class="slide-caption">OUR BUSINESS IS A MOBILE MASSAGE<br>SERVICE FOR GOLD COAST SENIORS</h2>
  <span class="slide-arrow prev"><svg width="8" height="14" viewBox="0 0 8 14"><path d="M7 1L1 7l6 6" fill="none" stroke="#aaa" stroke-width="1.3"/></svg></span>
  <span class="slide-arrow next"><svg width="8" height="14" viewBox="0 0 8 14"><path d="M1 1l6 6-6 6" fill="none" stroke="#fff" stroke-width="1.3"/></svg></span>
</section>
<div class="slider-shadow"></div>
<div class="dots"><i class="on"></i><i></i><i></i><i></i></div>

<section class="about">
  <h2 class="section-title" style="top:416px">ABOUT <em>GOLDEN YEARS MASSAGE</em></h2>
  <div class="title-rule" style="left:147px;width:436px;top:450px"></div>
  <p class="lead">Lorem ipsum dolor sit amet, conc tetur adipi scing. Praesent vestibuum molstie lacuiirhs. Aenean non ummy dreriauris. Phasellllus porta. Fusce suscipit variusium s molestie lacus.</p>
  <p class="body-copy">Lorem ipsum dolor sit amet, conc tetur adipi scing. Praesent vestibuum molstie lacuiirhs. Aenean non ummy dreriauris. Phasellllus porta. Fusce suscipit variusium sociis totdna tibus et magis dis parturient montes, nas. ceidiculus mus. Nulla dui. Fusce feugiatle. suada odio. Morbi nunc odio, gravida at. Cursus nec luctus a lorem. Lorem ipsum dolor sitat, consec tetuer adipiscing elit. Praesent vestibulum molestie lacus.</p>
  <a class="read-more-main" href="#">READ MORE</a>
</section>

<section class="services">
  <div class="services-band"></div>
  <h2 class="section-title" style="top:666px">OUR <em>MASSAGE SERVICES</em></h2>
  <div class="title-rule" style="left:198px;width:333px;top:702px"></div>

  <article class="service" style="left:45px">
    <div class="service-photo" role="img" aria-label="Therapist giving a foot reflexology massage" style="background:radial-gradient(circle at 45% 40%, #e8e2d8, #9fb7bf)"></div>
    <h3>Reflaxology</h3>
    <p>Lorem ipsum dolor sit amet,<br>consectetuer adipiscing elit, sed sit<br>amet, consectetuer nibh.</p>
    <a href="#">Read More</a>
  </article>
  <article class="service" style="left:202px">
    <div class="service-photo" role="img" aria-label="Therapist giving a shiatsu back massage" style="background:radial-gradient(circle at 50% 60%, #f4f2ee, #b8ab98)"></div>
    <h3>Shiatsu</h3>
    <p>Lorem ipsum dolor sit amet,<br>consectetuer adipiscing elit, sed sit<br>amet, consectetuer nibh.</p>
    <a href="#">Read More</a>
  </article>
  <article class="service" style="left:361px">
    <div class="service-photo" role="img" aria-label="Senior woman receiving a remedial shoulder massage" style="background:radial-gradient(circle at 50% 50%, #f3dfd0, #d9b59c)"></div>
    <h3>Remedial</h3>
    <p>Lorem ipsum dolor sit amet,<br>consectetuer adipiscing elit, sed sit<br>amet, consectetuer nibh,</p>
    <a href="#">Read More</a>
  </article>
  <article class="service" style="left:521px">
    <div class="service-photo" role="img" aria-label="Senior woman enjoying a relaxing face massage" style="background:radial-gradient(circle at 50% 50%, #efd6c6, #b88a72)"></div>
    <h3>Relaxation</h3>
    <p>Lorem ipsum dolor sit amet,<br>consectetuer adipiscing elit, sed sit<br>amet, consectetuer nibh,</p>
    <a href="#">Read More</a>
  </article>
</section>

<footer>
  <a class="brand footer-brand" href="#">
    <span class="brand-mark"></span>
    <span class="brand-name">GOLDEN YEARS MASSAGE</span>
  </a>
  <nav class="footer-nav">
    <a href="#">HOME</a>
    <a href="#">MASSAGE SERVICES</a>
    <a class="jp" href="#">ホーム</a>
    <a href="#">CONTACT US</a>
  </nav>
  <div class="social" aria-label="Social links"><i></i><i></i><i></i></div>
  <div class="copyright">Copyright © 2017 Goldenyearsmassage. All Right Reserved.</div>
</footer>

</body>
</html>
```